Business Card Design for Small Electrical Contractor

I need to update my business card into something a little more modern. We are a small electrical contracting company. We service domestic and commercial places around Sydney. We have 2 logo designs at the moment. I have uploaded both and 2 different sizes to work with.

Industry/Entity Type

Business

Contact Information for Business Card

Leo Hartigan
8/21-23 Birch Rd, Kelsworth 2087
t - (02) 9381 4720
m - 0427 815 903
E - info@hartiganelx.com.au
W - hartiganelx.com.au
ABN: 42 907 551 316

Font styles to use
Sans Serif

Requirements
Must have
• I would also like to see the below fit on somewhere aswell
• - Licensed Electrician
• - Level 2 (Cat 1 & 4)
• - Domestic
• - Commercial
• - Repairs and Installations
• - Data
Nice to have
• Try and keep similar colours as logo
Should not have
• No lightning bolts or light globes. Smart and professional please.

```html
<!DOCTYPE html>
<html lang="en">
<head>
<meta charset="utf-8">
<title>Hartigan Electrical – Business Card</title>
<link rel="stylesheet" href="https://fonts.googleapis.com/css2?family=Open+Sans:wght@400;600;700&display=swap">
<style>
  :root {
    --page: #e7e4e0;
    --card: #1c1c1c;
    --ink: #f2f2f2;
    --ink-soft: #d9d9d9;
    --accent: #e9a12a;
  }
  * { margin: 0; padding: 0; box-sizing: border-box; }
  html, body {
    width: 1200px; height: 900px; overflow: hidden;
    background: var(--page);
    font-family: "Open Sans", Arial, sans-serif;
  }
  .sheet {
    width: 1200px; height: 900px;
    display: flex; flex-direction: column;
    align-items: center; justify-content: center; gap: 24px;
  }
  .card {
    position: relative;
    width: 700px; height: 400px;
    background: var(--card);
    color: var(--ink);
    box-shadow: 0 6px 18px rgba(0,0,0,.25);
  }

  /* Front */
  .brand {
    position: absolute; left: 50px; top: 100px;
    font-size: 38px; font-weight: 600; letter-spacing: .5px;
    color: var(--ink); line-height: 1;
  }
  .rule-main {
    position: absolute; left: 50px; right: 40px; top: 160px;
    height: 2px; background: var(--accent);
  }
  .person {
    position: absolute; right: 40px; top: 112px; text-align: right;
  }
  .person-name {
    font-size: 19px; font-weight: 700; color: var(--accent);
  }
  .credentials {
    position: absolute; right: 40px; top: 174px; text-align: right;
    list-style: none; font-size: 12.5px; line-height: 1.55; color: var(--ink-soft);
  }
  .rule-contact {
    position: absolute; left: 50px; top: 262px;
    width: 250px; height: 2px; background: var(--accent);
  }
  .contacts {
    position: absolute; left: 50px; top: 272px;
    list-style: none; font-size: 15px; line-height: 1.6; color: var(--ink);
  }
  .contacts li { display: flex; align-items: center; gap: 8px; }
  .contacts svg { width: 14px; height: 14px; fill: var(--accent); flex: none; }

  /* Back */
  .card-back { display: flex; align-items: center; justify-content: center; }
  .back-brand { text-align: center; }
  .back-brand .brand { position: static; font-size: 46px; }
  .back-brand .rule { height: 2px; background: var(--accent); margin-top: 18px; }
</style>
</head>
<body>
<main class="sheet">

  <section class="card card-front" aria-label="Business card front">
    <div class="brand">Hartigan Electrical</div>
    <div class="person">
      <div class="person-name">Leo Hartigan</div>
    </div>
    <div class="rule-main"></div>
    <ul class="credentials">
      <li>Licensed Electrician</li>
      <li>Level 2 (Cat 1 &amp; 4)</li>
      <li>Domestic</li>
      <li>Commercial</li>
      <li>Repairs and Installations</li>
      <li>Data</li>
    </ul>

    <div class="rule-contact"></div>
    <ul class="contacts">
      <li>8/21-23 Birch Rd, Kelsworth 2087</li>
      <li>
        <svg viewBox="0 0 16 16" aria-hidden="true"><path d="M2 5c0-2 2-3 6-3s6 1 6 3v1h-3V5H5v1H2zM3 7h10l1 7H2zM8 9a2 2 0 1 0 0 4 2 2 0 0 0 0-4z"/></svg>
        (02) 9381 4720
      </li>
      <li>
        <svg viewBox="0 0 16 16" aria-hidden="true"><path d="M4 1h8v14H4zM5.5 3v9h5V3zM7 13h2v1H7z" fill-rule="evenodd"/></svg>
        0427 815 903
      </li>
      <li>
        <svg viewBox="0 0 16 16" aria-hidden="true"><path d="M1 3h14v10H1zM2 4l6 5 6-5z"/></svg>
        info@hartiganelx.com.au
      </li>
      <li>ABN: 42 907 551 316</li>
    </ul>
  </section>

  <section class="card card-back" aria-label="Business card back">
    <div class="back-brand">
      <div class="brand">Hartigan Electrical</div>
      <div class="rule"></div>
    </div>
  </section>

</main>
</body>
</html>
```